Information One Page for Email

I am looking for a informative attachment I can send with an introductive email for Ridgeview Cable Works. Something I can also Mail.

Ridgeview Cable Works is the leader in Rebar Post Tension Cable Placement and Post Tension Cable repair. Outside of cable placement and repair we do concrete repair, Parking Garage restoration and

Content

Post Tension Repair and Concrete Restoration
Post-tensioning is a revolutionary method in concrete construction that enhances the strength and durability of structures. However, like all construction ele-ments, post-tension cables can experience wear and damage over time. Ensuring timely and effective repair is crucial for maintaining the safety and integrity of your building.
Why Post-Tension Cable Repair is Essential
1. **Structural Integrity**: Damaged or deteriorated cables can compromise the structural integrity of your building, leading to safety hazards and potential structural failures.
2. **Extended Lifespan**: Regular maintenance and repair of post-tension cables extend the lifespan of your structure, ensuring it remains safe and function-al for years to come.
3. **Cost-Effective**: Addressing cable issues early on prevents more severe damage and costly repairs down the line.
Common Signs of Post-Tension Cable Issues
- Cracks in concrete surfaces
- Unusual noises or popping sounds
- Visible cable ends or broken strands
- Water leakage through cracks
Our Repair Process
1. **Inspection and Assessment**: Our team conducts a thorough inspection to identify the extent of the damage and determine the appropriate repair meth-ods.
2. **Cable Repair or Replacement**: Depending on the severity, we either re-pair the existing cables or replace them with new ones to restore full functional-ity.
3. **Sealing and Protection**: After repairing, we seal the affected areas to protect against moisture and future damage.
4. **Quality Assurance**: We perform rigorous quality checks to ensure the repairs meet industry standards and the structure is safe for use.
Why Choose Us
- **Expertise and Experience**: With years of experience in post-tension cable repair, our team is skilled in handling even the most complex repairs efficiently and effectively.
- **Advanced Technology**: We use the latest technology and materials to ensure durable and long-lasting repairs.
- **Customer Satisfaction**: Our commitment to quality and customer satisfaction sets us apart. We work closely with our clients to ensure their needs are met and expectations exceeded.
Contact Us
If you suspect issues with your post-tension cables or need a routine inspection, don't hesitate to contact us. Our experts are ready to provide the best solutions to keep your structures safe and secure.
Ensure the safety and longevity of your building with our professional post-tension cable repair services. Trust us to deliver quality and reliability every time.

```html
<!DOCTYPE html>
<html lang="en">
<head>
<meta charset="utf-8">
<title>Ridgeview Cable Works – Tension Repair and Concrete Restoration</title>
<link href="https://fonts.googleapis.com/css2?family=Poppins:wght@400;500;600;700&family=Arimo:wght@400;700&display=swap" rel="stylesheet">
<style>
  :root {
    --backdrop: #444444;
    --page: #ececec;
    --card: #fbfbfb;
    --ink: #111111;
    --muted: #555555;
    --brand-green: #13693e;
    --white: #ffffff;
    --photo-light: #d9dcdc;
    --photo-mid: #a7aaa6;
    --photo-dark: #6f716c;
  }
  * { box-sizing: border-box; margin: 0; padding: 0; }
  html, body { width: 910px; height: 1200px; overflow: hidden; }
  body { background: var(--backdrop); font-family: "Poppins", sans-serif; position: relative; }

  .flyer {
    position: absolute; left: 106px; top: 106px;
    width: 698px; height: 988px;
    background: var(--page); overflow: hidden;
  }

  .brand {
    position: absolute; left: 36px; top: 42px;
    display: flex; align-items: flex-start; gap: 10px;
  }
  .brand-square { width: 14px; height: 14px; background: var(--brand-green); margin-top: 10px; }
  .brand-name {
    color: var(--brand-green); font-weight: 600;
    font-size: 32px; line-height: 36px;
  }

  .hero-photo {
    position: absolute; left: 276px; top: 0;
    width: 422px; height: 420px;
    background: linear-gradient(135deg, var(--photo-light) 0%, var(--photo-mid) 55%, var(--photo-dark) 100%);
    clip-path: polygon(43% 0, 100% 0, 100% 100%, 0 100%, 8% 88%, 20% 60%, 30% 35%);
  }

  .headline {
    position: absolute; left: 35px; top: 208px;
    font-weight: 700; font-size: 39px; line-height: 42px;
    color: var(--ink); letter-spacing: -0.2px;
  }
  .headline .accent { color: var(--brand-green); }

  .intro {
    position: absolute; left: 35px; top: 390px; width: 190px;
    font-size: 10.4px; line-height: 12.6px; color: var(--ink);
    text-align: justify;
  }

  .info-card {
    position: absolute; left: 35px; width: 190px;
    background: var(--card); padding: 10px 12px;
    font-family: "Arimo", sans-serif; color: var(--muted);
  }
  .info-card.services { top: 530px; height: 208px; }
  .info-card.specialties { top: 748px; height: 209px; }
  .info-card h3 { font-size: 14px; font-weight: 700; margin-bottom: 14px; }
  .info-card p { font-size: 8.6px; line-height: 13.2px; margin-bottom: 13px; }
  .info-card ul { list-style: disc; padding-left: 12px; font-size: 8.6px; line-height: 13.2px; }
  .info-card ul ul { padding-left: 13px; }

  .why-panel {
    position: absolute; left: 280px; top: 419px;
    width: 418px; height: 569px;
    background: var(--brand-green); color: var(--white);
    padding: 18px 34px 0 22px;
  }
  .why-panel h2 { font-size: 23px; line-height: 26px; font-weight: 600; margin-bottom: 26px; }
  .reason h4 { font-size: 17px; line-height: 18px; font-weight: 600; }
  .reason p { font-size: 10.3px; line-height: 12.6px; text-align: justify; }
  .reason + .reason { margin-top: 14px; }
  .reason.cost { margin-top: 28px; }
  .signs { list-style: none; font-size: 10.3px; line-height: 12.6px; margin-top: 12px; }

  .contact-rule {
    position: absolute; left: 22px; top: 423px; width: 353px;
    border-top: 1px dashed rgba(255,255,255,0.8);
  }
  .contact-copy {
    position: absolute; left: 22px; top: 434px; width: 353px;
    font-size: 10.3px; line-height: 12.6px; text-align: justify;
  }
  .call {
    position: absolute; left: 22px; top: 518px;
    font-size: 24px; font-weight: 600; letter-spacing: 0.2px;
  }
</style>
</head>
<body>
  <main class="flyer">
    <header class="brand">
      <span class="brand-square"></span>
      <div class="brand-name">Ridgeview<br>Cable Works<br>LLC</div>
    </header>

    <div class="hero-photo" role="img" aria-label="Photograph of a concrete parking structure under repair, with shored slab edges and exposed post-tension cables"></div>

    <h1 class="headline">Tension<br>Repair<br>and <span class="accent">Concrete</span><br><span class="accent">Restoration</span></h1>

    <p class="intro">Post-tensioning is a revolutionary method in concrete construction that enhances the strength and durability of structures. However, like all construction ele-ments, post-tension cables can experience wear and damage over time. Ensuring timely and effective repair is crucial for maintaining the safety and integrity of your building.</p>

    <section class="info-card services">
      <h3>Services</h3>
      <ul>
        <li>Post Tension Repair</li>
        <li>Post Tension Restoration</li>
        <li>New Construction Reinforcing Installation</li>
        <li>Post Tension Consulting</li>
        <li>GPR Ground Penetrating Radar</li>
        <li>Barrier Cable:
          <ul>
            <li>Supply</li>
            <li>Install</li>
            <li>Replace</li>
            <li>Design &amp; Consulting</li>
          </ul>
        </li>
      </ul>
    </section>

    <section class="info-card specialties">
      <h3>Project Specialties</h3>
      <p>Helping Contractors, Condo Associations, Property Managers &amp; Developers with their construction projects including:</p>
      <ul>
        <li>High Rise Office Buildings</li>
        <li>Parking Garages</li>
        <li>Condominiums
          <ul>
            <li>New Construction</li>
            <li>Restoration</li>
          </ul>
        </li>
        <li>Post Tension Slab on Grade</li>
      </ul>
    </section>

    <section class="why-panel">
      <h2>Why Post-Tension Cable<br>Repair is Essential</h2>
      <div class="reason">
        <h4>Structural Integrity</h4>
        <p>Damaged or deteriorated cables can compromise the structural integrity of your building, leading to safety hazards and potential structural failures.</p>
      </div>
      <div class="reason">
        <h4>Extended Lifespan</h4>
        <p>Regular maintenance and repair of post-tension cables extend the lifespan of your structure, ensuring it remains safe and function-al for years to come.</p>
      </div>
      <div class="reason cost">
        <h4>Cost-Effective</h4>
        <p>Addressing cable issues early on prevents more severe damage and costly repairs down the line.<br>Common Signs of Post-Tension Cable Issues</p>
        <ul class="signs">
          <li>- Cracks in concrete surfaces</li>
          <li>- Unusual noises or popping sounds</li>
          <li>- Visible cable ends or broken strands</li>
          <li>- Water leakage through cracks</li>
        </ul>
      </div>

      <div class="contact-rule"></div>
      <p class="contact-copy">If you suspect issues with your post-tension cables or need a routine inspection, don't hesitate to contact us. Our experts are ready to provide the best solutions to keep your structures safe and secure. Ensure the safety and longevity of your building with our professional post-tension cable repair services. Trust us to deliver quality and reliability every time.</p>
      <div class="call">CALL (555) 014-2290</div>
    </section>
  </main>
</body>
</html>
```